依頼詳細
◇サイトマップ
①Home
②MENU&PRICE
③SALON INFO
④PRODUCTS
⑤COUPON
⑥GALLERY
⑦STAFF
⑧VOICE
⑨RECRUIT
⑩CONTACT
⑪BLOG(一覧)
⑫NEWS(一覧)
⑬CAT
⑭HAIR CARE

◇優先事項
1.ユーザビリティー
2.凝ったデザイン
3.編集更新

◇期待する効果
1.新規顧客の獲得
2.既存顧客の満足度向上
3.イメージアップ

◇ターゲット
【性別】男女比(男1 : 9女)
【年代】30代~40代
【属性】会社員 自営業 主婦

◇sns
SOCIALPAGE 会社用

◇テイスト
◯シンプル ナチュラル かっこいい
×可愛い・キュート カラフル 高級感

※デザインのテイストとして僕自身の好みですが、ペンキの質感やコンクリートの質感が好きで、シンプルの中にかっこよさがあるデザインが好きです。
(少しでも参考にして頂ければ嬉しいです)

◇希望カラー
ベース色(ベージュ・白)
差し色 (茶系・緑系 アースカラー)
サイトURL
http://mizutama2047.com/
ページ数
1ページ
希望イメージ
シンプル 複雑
単色 カラフル
暗い 明るい
日常 高級
遊び心 厳粛
未来的 伝統的
女性的 男性的
希望する色
茶系、緑系、グレー系、ペースは白系で考えています。そのほかは茶色や緑が好きです。
納品ファイル
• イラストレーター形式 (.ai)
• フォトショップ形式 (.psd)
• PNG形式 (.png)
補足説明
素材①
撮影データをナギボックスドライブにアップしています。
下記URLよりダウンロードしてください。
http://nagibox.jp/download/c51e7a02d9b3f684e10a7c2bd5f93e8a61c04d77
ダウンロードパスワード pass

※素材として、コンクリートの写真があり、店内の打ちっぱなしの部分になりますが、上手く背景などで使えたらと思い写真を取りました、使えなさそうであれば無視して頂いても構いません。

素材➁
クレパド:https://jp.krepado.com/
当院で定期契約をしています。クレジット購入のみのもの以外をご利用下さい。
また定期契約のものは当院の負担となり、ランサー様に負担はありません。
カンプ画像を入れてください。
依頼公開後の追記内容
素材のダウンロードリンクが切れてしまっていたので再度アップロード致します。
ダウンロードをお願い致します。
http://nagibox.jp/download/9e4c1b7a35d0f28e6a17c9b4e02d5f3a8b76c1e9

ダウンロードパスワード pass

作成期間が少なくなってしまった人もいるので延長させていただきます。
もう少し提案が見たいため、延長させて頂きます。
■ 選んだ理由

デザインが良かったので選定致しました。

■ 提案者全員のお礼・コメント

皆様素敵なデザインをありがとうございました。

```html
<!DOCTYPE html>
<html lang="ja">
<head>
<meta charset="utf-8">
<title>美容院 水玉</title>
<link href="https://fonts.googleapis.com/css2?family=Noto+Sans+JP:wght@300;400;500;700&family=Noto+Serif+JP:wght@700&display=swap" rel="stylesheet">
<style>
:root{
  --header-brown:#54473b;
  --intro-brown:#7b6c5b;
  --band-tan:#c8b387;
  --footer-brown:#6a5949;
  --paper:#ffffff;
  --ink:#222222;
  --soft-ink:#555555;
  --accent-green:#6f8f4e;
  --copyright-bg:#efebe4;
  --map-tone:#e6e2d8;
  --pin-red:#d94b3d;
  --table-line:#999999;
  --top-grey:#9a8f82;
}
*{margin:0;padding:0;box-sizing:border-box}
html,body{width:1200px;height:2556px;overflow:hidden}
body{position:relative;background:var(--paper);font-family:"Noto Sans JP",sans-serif;color:var(--ink)}
.abs{position:absolute}

.site-header{left:0;top:0;width:1200px;height:120px;background:linear-gradient(180deg,#5c4e41,var(--header-brown))}
.brand{left:30px;top:26px;display:flex;align-items:center;gap:14px;color:#fff;font-size:40px;font-weight:500;letter-spacing:4px}
.brand-dot{width:18px;height:18px;border-radius:50%;background:#fff}
.global-nav{right:60px;top:42px;display:flex;color:#fff;font-size:18px;font-weight:400}
.global-nav span{padding:0 14px;border-left:1px solid rgba(255,255,255,.7)}
.global-nav span:first-child{border-left:none}

.intro{left:0;top:120px;width:1200px;height:312px;background:linear-gradient(135deg,#85755f,var(--intro-brown) 60%,#716250);color:#fff;padding:46px 0 0 60px;font-size:29px;line-height:1.5;font-weight:400}

.main-column{left:0;top:432px;width:1008px}
.section-band{position:absolute;left:0;width:1008px;height:64px;background:var(--band-tan);color:#fff;font-size:34px;letter-spacing:3px;text-align:center;line-height:64px;font-weight:400}

.side-menu{left:1008px;top:432px;width:192px;padding:30px 0 0 22px}
.side-menu .home{font-size:38px;font-weight:300;margin-bottom:12px}
.side-menu li{list-style:none;font-size:19px;line-height:32px;font-weight:400}

.staff-card{position:absolute;width:310px}
.staff-photo{width:220px;height:220px;border-radius:50%;background:radial-gradient(circle at 50% 40%,#d8c6b0,#8c7a66);margin:0 auto}
.staff-name{text-align:center;font-size:18px;margin-top:12px;letter-spacing:2px}
.staff-text{font-family:"Noto Serif JP",serif;font-weight:700;font-size:18px;line-height:26px;margin-top:4px;white-space:nowrap}
.staff-more{font-family:"Noto Serif JP",serif;font-weight:700;font-size:18px;line-height:26px;text-align:right;white-space:nowrap}

.point{position:absolute;left:100px;font-size:21px;line-height:32px;display:flex;white-space:nowrap}
.point .label{width:130px}

.info-lines{left:220px;top:1396px;font-size:26px;line-height:36px}
.hours{left:220px;top:1508px;border-collapse:collapse;font-size:15px}
.hours td,.hours th{border:1px solid var(--table-line);height:38px;text-align:center;font-weight:400;width:44px}
.hours th.head,.hours td.head{width:130px}
.hours-note{left:400px;top:1632px;font-size:16px;line-height:24px}

.map{left:20px;top:1760px;width:968px;height:264px;background:linear-gradient(135deg,#eeeae2,var(--map-tone))}

.top-button{left:1032px;top:2044px;width:128px;height:48px;background:var(--top-grey);color:#fff;font-size:28px;text-align:center;line-height:48px;letter-spacing:2px}

.site-footer{left:0;top:2100px;width:1200px;height:380px;background:linear-gradient(160deg,#726150,var(--footer-brown))}
.footer-heading{color:#fff;font-size:22px;letter-spacing:1px}
.footer-heading::after{content:"";display:block;width:60px;height:3px;background:var(--accent-green);margin-top:4px}
.blog-list{left:80px;top:2200px;color:#fff;font-size:20px;line-height:40px;list-style:none}
.blog-list li{border-bottom:1px solid rgba(255,255,255,.35);width:420px}
.social-feed{left:680px;top:2180px;width:420px;height:260px;background:linear-gradient(180deg,#fafafa,#e9e9e9)}

.copyright{left:0;top:2480px;width:1200px;height:76px;background:var(--copyright-bg);text-align:center;line-height:76px;font-size:16px;color:var(--soft-ink)}
</style>
</head>
<body>

<header class="site-header abs">
  <div class="brand abs"><span class="brand-dot"></span>水玉</div>
  <nav class="global-nav abs"><span>STAFF</span><span>Recommended</span><span>SALON INFO</span><span>MAP</span><span>BLOG・SOCIALPAGE</span></nav>
</header>

<section class="intro abs">
  <p>青葉台駅前が最寄り駅の美容院「水玉」です。</p>
  <p>立体カットにこだわり３０年、アットホームなお店です！</p>
  <p>お客様の可愛い、綺麗を応援します！お気軽にお電話待っています！</p>
  <p>近くにはコンビニ、100円ショップあり、青葉台センタービルの二階にございます。</p>
</section>

<main class="main-column abs" style="height:1320px">
  <div class="section-band" style="top:0">STAFF</div>

  <div class="staff-card" style="left:68px;top:100px">
    <div class="staff-photo" role="img" aria-label="スタッフの写真"></div>
    <p class="staff-name">○○○○</p>
    <p class="staff-text">テキストテキストテキストテキスト<br>テキストテキストテキストテキスト<br>テキストテキストテキストテキスト<br>テキストテキストテキストテキスト</p>
    <p class="staff-more">もっと見る</p>
  </div>

  <div class="staff-card" style="left:448px;top:118px">
    <div class="staff-photo" role="img" aria-label="スタッフの写真"></div>
    <p class="staff-name">○○○○</p>
    <p class="staff-text">テキストテキストテキストテキスト<br>テキストテキストテキストテキスト<br>テキストテキストテキストテキスト<br>テキストテキストテキストテキスト</p>
    <p class="staff-more">もっと見る<br>他のスタッフを見る</p>
  </div>

  <div class="section-band" style="top:648px">Recommended</div>
  <div class="point" style="top:730px"><span class="label">1,Point 1</span><span>テキストテキストテキストテキストテキストテキストテキスト<br>テキストテキストテキストテキストテキストテキストテキスト</span></div>
  <div class="point" style="top:810px"><span class="label">2,Point 2</span><span>テキストテキストテキストテキストテキストテキストテキスト<br>テキストテキストテキストテキストテキストテキストテキスト</span></div>

  <div class="section-band" style="top:896px">SALON INFO</div>
</main>

<aside class="side-menu abs">
  <p class="home">Home</p>
  <ul>
    <li>MENU&amp;PRICE</li><li>NEWS(一覧)</li><li>CUT</li><li>HAIR CARE</li><li>PRODUCTS</li><li>COUPON</li><li>GALLERY</li><li>VOICE</li><li>BLOG(一覧)</li><li>CONTACT</li><li>RECRUIT</li>
  </ul>
</aside>

<div class="info-lines abs">
  <p>住所：〒123-4567 水玉県青葉市中央１丁目５－１８</p>
  <p>TEL：012-345-6789</p>
  <p>アクセス：青葉台駅から徒歩２分 /青葉台南駅から徒歩１０分</p>
</div>

<table class="hours abs">
  <tr><th class="head">受付時間</th><th>月</th><th>火</th><th>水</th><th>木</th><th>金</th><th>土</th><th>日</th><th>祝日</th></tr>
  <tr><td class="head">9:00 ～ 18:00</td><td></td><td>●</td><td>●</td><td>●</td><td>●</td><td>●</td><td></td><td></td></tr>
  <tr><td class="head">9:00 ～ 16:00</td><td></td><td></td><td></td><td></td><td></td><td></td><td>●</td><td>●</td></tr>
</table>
<p class="hours-note abs">定休日：毎週月曜及び第３月・火曜日</p>

<div class="section-band" style="top:1692px">MAP</div>
<div class="map abs" role="img" aria-label="サロン周辺の地図"></div>
<svg class="abs" style="left:480px;top:1850px" width="32" height="46" viewBox="0 0 32 46" aria-hidden="true">
  <path d="M16 0C7 0 0 7 0 16c0 12 16 30 16 30s16-18 16-30C32 7 25 0 16 0z" fill="var(--pin-red)"/>
  <circle cx="16" cy="16" r="6" fill="#fff"/>
</svg>

<div class="top-button abs">TOP</div>

<footer class="site-footer abs"></footer>
<div class="abs" style="left:80px;top:2150px"><p class="footer-heading">BLOG</p></div>
<ul class="blog-list abs">
  <li>201x/○x/○x　○○○○○○○○</li>
  <li>201x/○x/○x　○○○○○○○○</li>
  <li>201x/○x/○x　○○○○○○○○</li>
  <li>201x/○x/○x　○○○○○○○○</li>
  <li>201x/○x/○x　○○○○○○○○</li>
</ul>
<div class="abs" style="left:680px;top:2130px"><p class="footer-heading">SOCIALPAGE</p></div>
<div class="social-feed abs" role="img" aria-label="ソーシャルページの投稿フィード"></div>

<div class="copyright abs">copyright© MIZUTAMA Allrights reserved</div>

</body>
</html>
```